Pamphlet for introducing people to our church

I would like a church pamphlet designed, that includes the content in file "vosti-pamphlet.txt".

I am looking for a design that will incorporate the content in a professional and creative manner.

You do not have to use the content in any specific order, but I am relying on your skill and design knowledge to organize everything in an artistic and effective way.

Target Market(s)

Everyone

Industry/Entity Type

Religious

Requirements
Must have
• logo, use of content provided, use of branding (logo colors)
Nice to have
• More images where necessary
Should not have
• cross

```html
<!DOCTYPE html>
<html lang="en">
<head>
<meta charset="utf-8">
<title>Vosti – A Home for All Peoples</title>
<link rel="stylesheet" href="https://fonts.googleapis.com/css2?family=Cinzel:wght@400;500&family=Roboto:wght@400;500;700&display=swap">
<style>
  :root {
    --navy: #1d3a5f;
    --orange: #f7941d;
    --orange-deep: #e8821a;
    --ink: #1d3a5f;
    --rule: #9aa4b2;
    --page: #ffffff;
    --backdrop: #e4e6ea;
  }
  * { margin: 0; padding: 0; box-sizing: border-box; }
  html, body { width: 1200px; height: 650px; overflow: hidden; }
  body { background: var(--backdrop); font-family: "Roboto", Arial, sans-serif; }

  .flyer {
    position: absolute; left: 384px; top: 20px;
    width: 431px; height: 610px;
    background: var(--page);
    box-shadow: 0 10px 24px rgba(0,0,0,.25);
    overflow: hidden;
  }

  /* left column */
  .mission-panel {
    position: absolute; left: 0; top: 0; width: 162px; height: 100%;
    background: var(--navy); color: #fff; text-align: center;
  }
  .brand {
    position: absolute; top: 76px; left: 0; width: 100%;
    display: flex; align-items: center; justify-content: center; gap: 6px;
    font-family: "Cinzel", Georgia, serif; font-size: 31px; line-height: 34px; color: #fff;
  }
  .brand-dot { width: 8px; height: 8px; border-radius: 50%; background: var(--orange); }
  .mission-title {
    position: absolute; top: 150px; width: 100%;
    font-family: "Cinzel", Georgia, serif; font-weight: 400; font-size: 14px; line-height: 17px; letter-spacing: .5px;
  }
  .mission-rule { position: absolute; top: 192px; left: 67px; width: 28px; height: 1px; background: var(--orange); }
  .mission-body {
    position: absolute; top: 212px; left: 18px; right: 18px;
    font-size: 8.5px; line-height: 11.5px;
  }
  .mission-body p + p { margin-top: 11px; }
  .venue {
    position: absolute; top: 519px; width: 100%;
    font-size: 8.5px; line-height: 11.5px;
  }
  .venue strong { font-weight: 700; }

  /* right column */
  .hero { position: absolute; left: 162px; top: 0; }
  .faint-photo { position: absolute; left: 162px; top: 340px; }

  .headline { position: absolute; left: 184px; top: 280px; font-family: "Cinzel", Georgia, serif; }
  .headline-lead {
    display: flex; align-items: flex-end; gap: 8px;
    font-size: 19px; line-height: 22px; color: var(--orange-deep); letter-spacing: .3px;
  }
  .headline-main { font-size: 39px; line-height: 44px; color: var(--navy); letter-spacing: .5px; }
  .headline-rule { position: absolute; left: 184px; top: 352px; width: 220px; height: 1px; background: var(--rule); }

  .ministries-title {
    position: absolute; left: 184px; top: 368px;
    font-family: "Cinzel", Georgia, serif; font-weight: 400; font-size: 14px; color: var(--orange-deep); letter-spacing: .5px;
  }
  .ministry-list { position: absolute; left: 184px; top: 396px; width: 230px; list-style: none; color: var(--ink); }
  .ministry { position: relative; padding-left: 11px; font-size: 7.6px; line-height: 9.5px; margin-bottom: 10px; }
  .ministry::before {
    content: ""; position: absolute; left: 0; top: 1.5px;
    border-left: 6px solid var(--orange); border-top: 3.5px solid transparent; border-bottom: 3.5px solid transparent;
  }
  .ministry-name { font-weight: 500; text-transform: uppercase; display: block; }

  .service-band {
    position: absolute; left: 162px; top: 507px; width: 269px; height: 21px;
    background: var(--orange); color: #fff;
    font-size: 11.5px; font-weight: 700; line-height: 21px; padding-left: 22px; letter-spacing: .3px;
  }
  .contact-note {
    position: absolute; left: 184px; top: 541px; width: 240px;
    font-size: 6.6px; line-height: 9px; color: var(--ink); text-transform: uppercase;
  }
  .contact-note strong { font-weight: 700; }
  .footer-rule { position: absolute; left: 30px; top: 584px; width: 156px; height: 1px; background: var(--orange); }
  .website {
    position: absolute; left: 196px; top: 580px;
    font-size: 7px; line-height: 9px; letter-spacing: 2px; color: var(--ink);
  }
  .footer-brand {
    position: absolute; right: 16px; top: 576px;
    font-family: "Cinzel", Georgia, serif; font-size: 12px; line-height: 14px; color: var(--navy);
  }
</style>
</head>
<body>
  <article class="flyer">
    <aside class="mission-panel">
      <div class="brand"><span class="brand-dot"></span>VOSTI</div>
      <h2 class="mission-title">MISSION<br>STATEMENT</h2>
      <div class="mission-rule"></div>
      <div class="mission-body">
        <p>VOSTI is a family of people who come together to know God more deeply and to share His love with every neighbour. We welcome all who are searching, wherever they are on the journey, and we walk together in worship, prayer and the teachings of Jesus Christ.</p>
        <p>Our hope is a church that lives simply and loves well, with open doors and open hearts. We believe faith grows best in honest community, in service to others and in time spent with Scripture. We pray for a season of renewal in our city, marked by joy, generosity and lives changed by grace.</p>
      </div>
      <div class="venue">
        <strong>Harlow Community Hall</strong><br>
        48 Linden Street,<br>
        Brookfield, ME 04000<br>
        Visit us at www.vosti.org
      </div>
    </aside>

    <svg class="hero" width="269" height="300" viewBox="0 0 269 300">
      <defs>
        <linearGradient id="heroTone" x1="0" y1="0" x2="1" y2="1">
          <stop offset="0" stop-color="#2a2547"/>
          <stop offset=".5" stop-color="#5b4a7a"/>
          <stop offset="1" stop-color="#8a7a5c"/>
        </linearGradient>
      </defs>
      <polygon points="0,0 269,0 269,252 0,186" fill="url(#heroTone)" role="img" aria-label="Photo of a lit church tower at night beside a person praying with clasped hands"/>
      <polygon points="0,186 269,252 269,272 0,212" fill="#f7941d"/>
    </svg>

    <svg class="faint-photo" width="269" height="270" viewBox="0 0 269 270">
      <defs>
        <radialGradient id="faintTone" cx=".75" cy=".55" r=".6">
          <stop offset="0" stop-color="#c9ccd2" stop-opacity=".5"/>
          <stop offset="1" stop-color="#ffffff" stop-opacity="0"/>
        </radialGradient>
      </defs>
      <rect width="269" height="270" fill="url(#faintTone)" role="img" aria-label="Faint photo of a man kneeling in prayer in a field"/>
    </svg>

    <div class="headline">
      <div class="headline-lead">A HOME FOR ALL
        <svg width="30" height="30" viewBox="0 0 34 34" fill="none" stroke="#1d3a5f" stroke-width="1.6">
          <path d="M13 10 L17 4 L21 10 Z"/>
          <rect x="13" y="10" width="8" height="21"/>
          <path d="M3 31 V19 L13 14 M21 14 L31 19 V31 Z M3 31 H31"/>
          <rect x="15.5" y="24" width="3" height="7"/>
          <rect x="6" y="22" width="3" height="4"/>
          <rect x="25" y="22" width="3" height="4"/>
        </svg>
      </div>
      <div class="headline-main">PEOPLES</div>
    </div>
    <div class="headline-rule"></div>

    <h3 class="ministries-title">MINISTRIES</h3>
    <ul class="ministry-list">
      <li class="ministry"><span class="ministry-name">Little Lights (Children's Ministry)</span>Kids explore Bible stories through play, song and friendship.</li>
      <li class="ministry"><span class="ministry-name">Foundations Class</span>A friendly start for anyone curious about faith and what it means today.</li>
      <li class="ministry"><span class="ministry-name">Growth Circles</span>Small groups that read Scripture together and learn to serve others.</li>
    </ul>

    <div class="service-band">SUNDAY SERVICE: 10:00AM-12:30PM</div>
    <p class="contact-note">If you need prayer or counseling give us a call at<br><strong>+1 555-010-2480</strong> or email us at <strong>hello@vostichurch.org</strong></p>

    <div class="footer-rule"></div>
    <div class="website">WWW.VOSTI.ORG</div>
    <div class="footer-brand">VOSTI</div>
  </article>
</body>
</html>
```